Packaging for nuts & dried fruits products

We need a packaging design for our nuts and dried fruits product in a stand-up pouch with 23x13cm size. We repack and/or process almonds, sliced almonds, walnuts, pistachios, cashews, dried blueberries, dried cranberries, and dried mangoes. We need the design to look fresh, premium, and professional. We would like to see designs that use color green but with color combinations of either beige, gray, or black.

See on the upload files a sample of what we've initially done. NOTE that the white space on the front will be a "window" where the products can be seen by consumers and the design/colors used to be catchy.

The challenge here is the product name (ex. Walnuts) will NOT be printed on the packaging itself but will be labelled using stickers - meaning this will be a generic template for all our products.

SC Back and SC_Front images are our initial designs, while the rest are images from the internet for references.

Target Market(s)

Market are for athletic individuals, health conscious, fresh/organic food buyers.
Middle to upper market.

Industry/Entity Type

Product

Colors
abd036
9bcb3c

Requirements
Must have
• 1. A "window" or see through area for the product.
• 2. Healthy, fresh, and natural concept.
• 3. There must be a FRONT and BACK design submitted.
• 4. Design must be appropriate for printing on a Stand-up resealable pouch (see uploaded Sample_packaging.jpg).
• 5. All information at SC_Back image must be on back design as well.
• 6. Storage and Allergy information must be at the back.
• 7. Leave an area for barcode.
Nice to have
• 1. Outlines/emboss of nuts (walnuts, cashews, almonds, pistachios, blueberries, cranberries).
• 2. Put "Great for snacks and baking!" at the front.
• 3. Put "Resealable to contain freshness" at the top of the packaging.
Should not have
• 1. Should not have a product label or packaging size on the design (ex. Walnuts 500g).
• 2. Should not use "heart" shapes.

```html
<!DOCTYPE html>
<html lang="en">
<head>
<meta charset="utf-8">
<title>Nuts &amp; Dried Fruits Pouch – Front and Back</title>
<link href="https://fonts.googleapis.com/css2?family=Lilita+One&family=Source+Sans+3:ital,wght@0,400;0,600;0,700;1,700&display=swap" rel="stylesheet">
<style>
  :root{
    --lime:#abd036;
    --green:#9bcb3c;
    --deep:#5c9a2f;
    --forest:#4f8a2a;
    --pale:#d5e67c;
    --maroon:#5b1a14;
    --ink:#2b2b2b;
    --rule:#333;
    --mist:#b4b4b4;
    --white:#fff;
  }
  *{box-sizing:border-box;margin:0;padding:0}
  html,body{width:1200px;height:1087px;overflow:hidden;background:var(--white)}
  body{position:relative;font-family:"Source Sans 3",Arial,sans-serif;color:var(--ink)}

  /* dimension marks */
  .dim-h{position:absolute;height:12px;border-left:1px solid var(--rule);border-right:1px solid var(--rule)}
  .dim-h::after{content:"";position:absolute;left:0;right:0;top:5px;border-top:1px solid var(--rule)}
  .dim-v{position:absolute;width:12px;border-top:1px solid var(--rule);border-bottom:1px solid var(--rule)}
  .dim-v::after{content:"";position:absolute;top:0;bottom:0;left:5px;border-left:1px solid var(--rule)}
  .dim-label{position:absolute;font-size:22px;color:var(--ink)}
  .dim-label.vert{transform:rotate(-90deg);transform-origin:center}
  .side-caption{position:absolute;top:950px;font-size:21px}

  /* front panel */
  .pouch{position:absolute;top:150px;width:445px;height:786px;overflow:hidden}
  .front{left:132px;background:var(--lime);border:1px solid #888}
  .nut-doodles{position:absolute;left:0;top:40px;width:100%;height:560px;
    background:linear-gradient(180deg,rgba(150,185,50,.35),rgba(150,185,50,.15))}
  .center-band{position:absolute;left:92px;top:0;width:266px;height:540px;background:var(--green);
    box-shadow:0 0 14px rgba(40,80,10,.35)}
  .reseal{position:absolute;left:103px;top:73px;width:244px;height:19px;border:1px solid #f4f8e0;
    font:italic 700 11.5px/17px "Source Sans 3",Arial,sans-serif;color:#1f2b10;text-align:center;letter-spacing:.3px}
  .snack-tag{position:absolute;left:52px;top:238px;width:290px;height:200px;background:var(--pale);
    transform:rotate(-8deg);box-shadow:0 3px 8px rgba(0,0,0,.2)}
  .snack-tag::before{content:"";position:absolute;inset:9px;border:1.5px dashed var(--maroon)}
  .snack-tag h1{position:absolute;left:0;right:0;top:22px;text-align:center;
    font:400 46px/50px "Lilita One",Impact,sans-serif;color:var(--maroon);letter-spacing:.5px}
  .window{position:absolute;left:0;top:520px;width:100%;height:266px;background:var(--white)}
  .window svg{display:block}
  .produce{position:absolute;left:0;top:425px}

  /* back panel */
  .back{left:623px;background:var(--green)}
  .back-inner{position:absolute;left:20px;top:0;width:405px;height:786px;background:var(--lime);
    box-shadow:0 0 16px rgba(40,80,10,.45)}
  .claims{position:absolute;left:196px;top:44px;width:209px}
  .claims li{list-style:none;height:30px;margin-bottom:4px;background:var(--deep);
    font:700 26px/30px "Source Sans 3",Arial,sans-serif;color:var(--white);padding-left:14px;letter-spacing:.5px}
  .seal{position:absolute;left:96px;top:38px;width:96px;height:96px;border-radius:50%;
    background:var(--deep);border:2px solid var(--white)}
  .white-zone{position:absolute;left:0;top:205px;width:398px;height:214px;background:var(--white)}
  .back-produce{position:absolute;left:6px;top:150px}
  .intro{position:absolute;left:16px;top:300px;width:372px;font-size:14.3px;line-height:17.5px;text-align:justify;color:#222}
  .intro p+p{margin-top:17px}
  .slogan{position:absolute;left:0;top:420px;width:398px;height:50px;background:var(--green);
    text-align:center;font:italic 700 16px/19px "Source Sans 3",Arial,sans-serif;color:var(--white);padding-top:6px}
  .care{position:absolute;left:0;top:470px;width:405px;height:130px;background:var(--forest);color:var(--white);padding:6px 18px}
  .care h2{font-size:14px;font-weight:700;letter-spacing:.3px;display:inline-block;border-bottom:1.5px solid var(--white);padding-right:16px;line-height:17px}
  .care p{font-size:11.2px;line-height:14px;margin-top:3px}
  .care h2+p{margin-bottom:7px}
  .contact{position:absolute;left:16px;top:620px;width:190px;font-size:8.6px;line-height:11px;color:#1e2a10}
  .handle{display:flex;align-items:center;gap:5px;margin-bottom:9px}
  .handle i{display:inline-block;width:9px;height:9px;border-radius:50%;background:var(--forest)}
  .contact address{font-style:normal}
  .barcode-slot{position:absolute;left:207px;top:626px;width:185px;height:130px;background:var(--white)}
  .barcode-slot span{position:absolute;left:0;right:0;top:55px;text-align:center;font-size:8.8px;line-height:11px;color:#222}
</style>
</head>
<body>

<!-- dimension marks -->
<div class="dim-h" style="left:132px;top:110px;width:446px"></div>
<div class="dim-label" style="left:328px;top:72px">13 cm</div>
<div class="dim-h" style="left:623px;top:110px;width:445px"></div>
<div class="dim-label" style="left:818px;top:72px">13 cm</div>
<div class="dim-v" style="left:90px;top:150px;height:786px"></div>
<div class="dim-label vert" style="left:50px;top:526px">23 cm</div>
<div class="dim-v" style="left:1098px;top:150px;height:786px"></div>
<div class="dim-label vert" style="left:1100px;top:500px">23 cm</div>

<!-- FRONT -->
<section class="pouch front" aria-label="Pouch front">
  <div class="nut-doodles" role="img" aria-label="Line drawings of nuts and dried fruits scattered across the background"></div>
  <div class="center-band"></div>
  <div class="reseal">RESEALABLE TO CONTAIN FRESHNESS</div>
  <div class="snack-tag"><h1>GREAT FOR<br>SNACKS &amp;<br>BAKING!</h1></div>

  <div class="window">
    <svg width="445" height="266" aria-label="Clear see-through window">
      <defs>
        <pattern id="see-through" width="92" height="11" patternUnits="userSpaceOnUse">
          <text x="0" y="9" font-family="Source Sans 3, Arial, sans-serif" font-size="10" fill="#b4b4b4">see through area •</text>
        </pattern>
      </defs>
      <rect x="0" y="0" width="445" height="266" fill="url(#see-through)"/>
    </svg>
  </div>

  <svg class="produce" width="445" height="200" role="img" aria-label="Photo of blueberries, almonds, walnuts and cashews spilling above the window">
    <defs>
      <linearGradient id="nut-tone" x1="0" x2="1" y1="0" y2="0">
        <stop offset="0" stop-color="#2f3f7a"/>
        <stop offset=".17" stop-color="#3b4b86"/>
        <stop offset=".25" stop-color="#8a5a34"/>
        <stop offset=".55" stop-color="#b5703f"/>
        <stop offset=".8" stop-color="#d9a560"/>
        <stop offset="1" stop-color="#e2b46e"/>
      </linearGradient>
    </defs>
    <path d="M0 115 Q10 88 50 86 Q90 60 150 62 Q210 45 270 55 Q340 45 400 62 Q440 72 445 100 L445 128 Q420 150 380 140 Q330 165 280 160 Q250 205 222 198 Q200 165 170 170 Q120 175 95 160 Q60 145 30 150 Q10 150 0 140 Z" fill="url(#nut-tone)"/>
  </svg>
</section>
<div class="side-caption" style="left:132px">Front Side</div>

<!-- BACK -->
<section class="pouch back" aria-label="Pouch back">
  <div class="back-inner">
    <ul class="claims"><li>NATURAL</li><li>FRESH</li><li>HEALTHY</li></ul>

    <div class="white-zone"></div>
    <svg class="back-produce" width="392" height="140" role="img" aria-label="Photo of blueberries, almonds, walnuts and cashews">
      <defs>
        <linearGradient id="nut-tone-back" x1="0" x2="1">
          <stop offset="0" stop-color="#2f3f7a"/>
          <stop offset=".16" stop-color="#3b4b86"/>
          <stop offset=".24" stop-color="#9a5e34"/>
          <stop offset=".6" stop-color="#a8733f"/>
          <stop offset=".8" stop-color="#deab66"/>
          <stop offset="1" stop-color="#e6ba74"/>
        </linearGradient>
      </defs>
      <path d="M2 70 Q20 38 70 42 Q120 18 190 24 Q260 10 330 28 Q380 34 390 70 Q392 95 360 100 Q300 120 240 112 Q180 134 130 115 Q80 112 50 98 Q10 98 2 70 Z" fill="url(#nut-tone-back)"/>
    </svg>

    <div class="seal" aria-hidden="true"></div>

    <div class="intro">
      <p>Our premium nuts and dried fruits are perfect for snacking, backing and supplementing your healthy nutritional choices !</p>
      <p>Enjoy and share every pack without the guilt since our nuts are prepared with low or no salt at all and our dried fruits have no added sugar.</p>
    </div>

    <div class="slogan">All Natural. all fresh.<br>your body will know the difference</div>

    <div class="care">
      <h2>STORAGE INFORMATION</h2>
      <p>Keep in a cool dry place to maintain freshness &amp; shelf life.<br>Do Not expose to heat or sunlight that may cause reduced shelf life or nuts to taste rancid.</p>
      <h2>FOOD ALLGERY WARNING</h2>
      <p>This product may contain nut ingredients.</p>
    </div>

    <div class="contact">
      <div class="handle"><i></i>facebook.com/greengrovesnacks</div>
      <div class="handle"><i></i>@greengrovesnacks</div>
      <div class="handle"><i></i>@thegreengrovesnacks</div>
      <address>Packaged and Distributed by<br>Verdant Pantry Trading<br>Mabini Lane Block 7, Riverside City, 2040<br>(+632) 555 0142, (+63) 900 555 0187<br>verdantpantry@example.com</address>
    </div>

    <div class="barcode-slot">
      <svg width="185" height="130" aria-hidden="true">
        <g stroke="#333" stroke-width="1" stroke-dasharray="5 4">
          <line x1="12" y1="10" x2="70" y2="52"/><line x1="173" y1="10" x2="115" y2="52"/>
          <line x1="12" y1="120" x2="70" y2="80"/><line x1="173" y1="120" x2="115" y2="80"/>
        </g>
      </svg>
      <span>Space for Barcode and<br>Product Exp details</span>
    </div>
  </div>
</section>
<div class="side-caption" style="left:623px">Back Side</div>

</body>
</html>
```